Prepared ready to cook meal delivery service needs a flyer design

We need a flyer design for a startup company based in Cape Town, South Africa. I've attached a few flyer designs that I like.

The company is called 'Brindle' and our website will be found at brindle.co.za. We don't have a logo yet.

Flyer text:

Brindle
Ready to roast

Do you feel like a home cooked meal but don't like shopping, peeling, chopping, cooking, or cleaning up?

We deliver ready to roast free range chicken and fresh vegetables to your door.

To order: SMS your name to 083 614 2958 and we'll call you back.

Only the best ingredients used
Free range chickens. Fresh herbs and vegetables. Virgin olive oil.

No bad carbs!

Ready to roast Free range chicken and fresh veggies
For 2 R99
For 4 R139
Updates

Wording of flyer updated.

Target Market(s)

Local Cape Townians that hate grocery shopping and need help saving time preparing meals.

Industry/Entity Type

Delivery Service

Requirements
Must have
• To find out more: SMS your name to 083 614 2958

```html
<!DOCTYPE html>
<html lang="en">
<head>
<meta charset="utf-8">
<title>Brindle – Ready to Roast Flyer</title>
<link rel="stylesheet" href="https://fonts.googleapis.com/css2?family=Bebas+Neue&family=Libre+Baskerville:ital,wght@0,400;1,700&family=PT+Sans:ital,wght@0,700;1,700&display=swap">
<style>
  :root {
    --stage: #ffffff;
    --olive-light: #c9d262;
    --olive: #b3c046;
    --olive-deep: #7e8a1e;
    --olive-dark: #4a4a12;
    --ink: #141414;
    --cream: #f4efd8;
    --band-cream: #e9e4cf;
    --red: #e2311d;
    --red-ring: #3a2410;
    --green: #3aa33a;
    --green-ring: #2f8a2a;
    --lime: #a9c43a;
    --yellow-text: #ecec6e;
    --gold: #c8b41c;
    --gold-ring: #8c7a1e;
    --price-fill: #cdd27a;
  }
  * { box-sizing: border-box; margin: 0; padding: 0; }
  html, body { width: 1200px; height: 831px; overflow: hidden; background: var(--stage); }
  .flyer {
    position: absolute; left: 310px; top: 0; width: 580px; height: 831px; overflow: hidden;
    background: radial-gradient(ellipse at 50% 40%, var(--olive-light), var(--olive) 75%);
    font-family: 'PT Sans', sans-serif;
  }
  .top-rule { position: absolute; left: 0; top: 0; width: 100%; height: 8px; background: var(--ink); }
  .intro {
    position: absolute; left: 28px; top: 32px; width: 340px; z-index: 3;
    font-family: 'Libre Baskerville', serif; font-style: italic; font-weight: 700;
    font-size: 17px; line-height: 1.4; color: var(--cream);
  }
  .brand-name {
    position: absolute; left: 28px; top: 124px; z-index: 3;
    font-family: 'Bebas Neue', sans-serif; font-weight: 400; font-size: 76px; line-height: 1; color: var(--ink); letter-spacing: 1px;
  }
  .tagline {
    position: absolute; left: 24px; top: 198px; z-index: 3;
    font-family: 'Bebas Neue', sans-serif; font-weight: 400; font-size: 56px; line-height: 1; color: var(--ink);
  }
  .dish-ring {
    position: absolute; left: 16px; top: 222px; width: 564px; height: 368px; border-radius: 50%;
    background: var(--olive-deep); z-index: 1;
  }
  .dish-photo {
    position: absolute; left: 32px; top: 236px; width: 540px; height: 342px; border-radius: 50% / 48%; z-index: 1;
    background:
      radial-gradient(ellipse at 45% 45%, #e8c07a 0%, #d39a4a 30%, transparent 55%),
      radial-gradient(ellipse at 30% 85%, #c8321e 0%, transparent 30%),
      radial-gradient(ellipse at 65% 85%, #e8c23a 0%, transparent 25%),
      linear-gradient(180deg, #f3efe6, #e4dccb);
  }
  .badge {
    position: absolute; z-index: 4; border-radius: 50%; display: flex; align-items: center; justify-content: center;
    text-align: center; font-family: 'Bebas Neue', sans-serif; line-height: 1.1;
    box-shadow: 4px 6px 10px rgba(0,0,0,.35);
  }
  .badge--delivery {
    left: 346px; top: 30px; width: 230px; height: 230px; background: var(--red);
    border: 5px solid var(--red-ring); color: #fff; font-size: 27px;
  }
  .badge--carbs {
    left: 94px; top: 270px; width: 88px; height: 88px; background: var(--cream);
    border: 5px solid var(--ink); color: var(--ink); font-size: 19px;
  }
  .badge--ingredients {
    left: 4px; top: 438px; width: 138px; height: 138px; background: var(--olive-dark);
    border: 4px solid #2e2e08; color: var(--yellow-text); font-size: 22px;
  }
  .badge--for2 {
    left: 434px; top: 290px; width: 142px; height: 142px; background: var(--lime);
    border: 6px solid var(--green-ring); color: var(--yellow-text); flex-direction: column;
  }
  .badge--for4 {
    left: 404px; top: 420px; width: 164px; height: 164px; background: var(--price-fill);
    border: 6px solid var(--gold-ring); color: var(--olive-dark); flex-direction: column;
  }
  .price-label { font-size: 34px; }
  .price { font-family: 'Libre Baskerville', serif; font-size: 44px; line-height: 1; }
  .price sup { font-size: 22px; vertical-align: 18px; }
  .badge--for4 .price { font-size: 48px; }
  .veggie-band {
    position: absolute; left: 0; top: 674px; width: 100%; height: 32px; background: var(--band-cream);
    font-family: 'Bebas Neue', sans-serif; font-size: 26px; line-height: 34px; color: var(--olive-dark);
    padding-left: 26px; letter-spacing: .3px;
  }
  .order-band { position: absolute; left: 0; top: 706px; width: 100%; height: 84px; background: var(--ink); }
  .order-label {
    position: absolute; left: 28px; top: 12px; font-style: italic;
    font-weight: 700; font-size: 25px; line-height: 1.2; color: #fff;
  }
  .order-panel {
    position: absolute; left: 116px; top: 6px; right: 0; height: 72px; background: var(--green);
    clip-path: polygon(0 0, 100% 0, 100% 100%, 22px 100%);
    color: var(--band-cream); font-weight: 700; font-size: 25px; line-height: 1.3; padding: 4px 0 0 26px;
  }
  .order-panel span { display: block; padding-left: 24px; }
  .web-band {
    position: absolute; left: 0; top: 790px; width: 100%; height: 41px; background: var(--gold);
    font-family: 'Bebas Neue', sans-serif; font-size: 27px; line-height: 42px; color: var(--olive-dark);
    text-align: center;
  }
</style>
</head>
<body>
  <main class="flyer">
    <div class="top-rule"></div>
    <p class="intro">Do you feel like a home cooked meal<br>but don't like shopping, peeling,<br>chopping, cooking, or cleaning up?</p>
    <h1 class="brand-name">BRINDLE</h1>
    <h2 class="tagline">READY TO ROAST</h2>

    <div class="dish-ring"></div>
    <div class="dish-photo" role="img" aria-label="Roast free range chicken in a white dish with red peppers, red onions, lemon and potatoes"></div>

    <div class="badge badge--delivery">WE<br>DELIVER READY TO<br>ROAST FREE RANGE<br>CHICKEN AND FRESH<br>VEGETABLES TO YOUR<br>DOOR.</div>
    <div class="badge badge--carbs">NO<br>BAD<br>CARBS!</div>
    <div class="badge badge--ingredients">ONLY<br>THE BEST<br>INGREDIENTS<br>USE</div>
    <div class="badge badge--for2">
      <span class="price-label">FOR 2</span>
      <span class="price"><sup>R</sup>99</span>
    </div>
    <div class="badge badge--for4">
      <span class="price-label">FOR 4</span>
      <span class="price"><sup>R</sup>139</span>
    </div>

    <div class="veggie-band">READY TO ROAST FREE RANGE CHICKEN AND FRESH VEGGIES</div>
    <div class="order-band">
      <p class="order-label">TO<br>ORDER:</p>
      <p class="order-panel">SMS your name to 083 614 2958<span>and we'll call you back.</span></p>
    </div>
    <div class="web-band">WWW.BRINDLE.CO.ZA</div>
  </main>
</body>
</html>
```